Website Design For Atelier Nine Design Group

Create a sophisticated website that denotes high-end luxury. We would like to keep the copy minimalist and elegantly understated while communicating only the most essential information. While creating an air of exclusivity.
We would like 3-4 Tab Wesbite
Home:
• Feature a design project front and centre, along with a short
introduction about who we are and what we do.

We can put a Call To Action at the end of the introduction inviting readers to learn more on our About page.
About:
• This page should provide more detail on our background, past
achievements, history of the company, and anything you'd like to
highlight.
• We should also provide details on our services, aesthetic, process, etc.
Team:
• introduce the team, possibly with short descriptions for each
team member. Total Team Members 7
Residential
• The portfolio page can be a grid of images along with titles for
each project.
• Clicking on each image should take you to a separate page for that
project where readers can find more details

Commercial
The portfolio page can be a grid of images along with titles for
each project.

Contact Us:

example website:
https://www.morvexinteriors.example/

Target Market(s)

High end luxury clientele

Industry/Entity Type

Interior Design

Number of Pages Required

4 page

Font styles to use
Sans Serif

Requirements
Must have
• Company logo, color scheme and name: Atelier Nine Design Group

```html
<!DOCTYPE html>
<html lang="en">
<head>
<meta charset="utf-8">
<title>Atelier Nine Design Group</title>
<link href="https://fonts.googleapis.com/css2?family=Barlow+Condensed:wght@500;600&family=Roboto:wght@400&display=swap" rel="stylesheet">
<style>
  :root {
    --navy: #06364a;
    --gold: #c9a04a;
    --ink: #1f1f1f;
    --rule: #dcdcdc;
    --mist: #f1f2f4;
    --white: #ffffff;
    --footer-rule: #1c4b5c;
    --display: "Barlow Condensed", "Arial Narrow", sans-serif;
    --body: "Roboto", Arial, sans-serif;
  }
  * { box-sizing: border-box; margin: 0; padding: 0; }
  html, body { width: 1200px; height: 2266px; overflow: hidden; background: var(--white); }
  body { position: relative; font-family: var(--body); color: var(--ink); }

  .site-header { position: absolute; top: 0; left: 0; width: 1200px; height: 229px; }
  .header-rule { position: absolute; left: 172px; width: 856px; height: 1px; background: var(--rule); }
  .header-rule.top { top: 118px; }
  .header-rule.bottom { top: 185px; }
  .brand { position: absolute; top: 14px; left: 520px; width: 160px; height: 112px; background: var(--white);
    display: flex; flex-direction: column; align-items: center; justify-content: center; gap: 6px; }
  .brand-mark { display: block; width: 26px; height: 26px; border: 4px solid var(--navy); }
  .brand-name { display: block; font-family: var(--display); font-weight: 600; color: var(--navy); font-size: 22px;
    letter-spacing: 2px; line-height: 1.05; text-align: center; text-transform: uppercase; }
  .main-nav { position: absolute; top: 138px; left: 0; width: 1200px; display: flex; justify-content: center; gap: 44px; }
  .main-nav a { font-family: var(--display); font-weight: 500; font-size: 21px; color: var(--navy);
    text-decoration: none; text-transform: uppercase; letter-spacing: .5px; }
  .main-nav a.active { color: var(--gold); }

  .project-strip { position: absolute; top: 229px; left: 0; width: 1200px; height: 652px; display: flex; }
  .project-photo { flex: 1; height: 100%; }
  .photo-living { background: linear-gradient(160deg, #2f4f45 0%, #cfc9bf 45%, #e7e2da 75%, #a9a39a 100%); }
  .photo-bath { background: linear-gradient(170deg, #9a9b9e 0%, #b8b9bb 45%, #e9e9ea 70%, #8e8c88 100%); }
  .photo-study { background: linear-gradient(165deg, #3e4646 0%, #6a6f6e 40%, #d9d4cb 70%, #a7aab0 100%); }

  .about-intro { position: absolute; top: 881px; left: 0; width: 1200px; height: 579px; text-align: center; }
  .intro-mark { position: absolute; top: 88px; left: 576px; width: 42px; height: 42px; border: 5px solid var(--navy); }
  .section-title { font-family: var(--display); font-weight: 600; color: var(--navy); font-size: 50px;
    letter-spacing: .5px; text-transform: uppercase; }
  .about-intro .section-title { position: absolute; top: 152px; width: 100%; }
  .intro-text { position: absolute; top: 240px; left: 133px; width: 934px; font-size: 15px; line-height: 22.5px; }
  .btn-outline { position: absolute; top: 410px; left: 518px; width: 164px; height: 54px; border: 2px solid var(--gold);
    font-family: var(--display); font-weight: 500; font-size: 28px; color: var(--gold); text-decoration: none;
    display: flex; align-items: center; justify-content: center; text-transform: uppercase; }

  .services { position: absolute; top: 1460px; left: 0; width: 1200px; height: 395px; background: var(--mist); }
  .services .section-title { position: absolute; top: 60px; width: 100%; text-align: center; }
  .service { position: absolute; top: 195px; width: 520px; height: 110px; }
  .service.commercial { left: 103px; }
  .service.residential { left: 640px; }
  .service-icon { position: absolute; left: 0; top: 0; width: 109px; height: 109px; }
  .service-name { position: absolute; left: 157px; top: 0; font-family: var(--display); font-weight: 500;
    font-size: 30px; color: var(--gold); text-transform: uppercase; line-height: 1.1; }
  .service-text { position: absolute; left: 157px; top: 50px; width: 345px; font-size: 15px; line-height: 22.5px; color: #2a2a2a; }

  .site-footer { position: absolute; top: 1855px; left: 0; width: 1200px; height: 411px; background: var(--navy); color: var(--white); }
  .footer-title { font-family: var(--display); font-weight: 600; font-size: 34px; text-transform: uppercase; line-height: 1; }
  .footer-contact { position: absolute; left: 99px; top: 88px; }
  .contact-list { list-style: none; margin-top: 22px; }
  .contact-list li { display: flex; align-items: flex-start; gap: 13px; font-size: 15px; line-height: 19px; margin-bottom: 14px; }
  .contact-icon { width: 31px; height: 31px; flex: none; }
  .contact-list span { padding-top: 2px; }
  .footer-brand { position: absolute; left: 430px; top: 90px; width: 340px; display: flex; flex-direction: column; align-items: center; }
  .footer-brand .brand-mark { width: 52px; height: 52px; border: 6px solid var(--white); margin-bottom: 22px; }
  .footer-brand .brand-name { color: var(--white); font-size: 40px; letter-spacing: 4px; line-height: 1.05; }
  .social-links { position: absolute; top: 275px; left: 525px; display: flex; gap: 12px; }
  .social-links span { width: 42px; height: 42px; border: 2px solid var(--white); border-radius: 50%; display: block; }
  .quick-links { position: absolute; left: 950px; top: 88px; }
  .quick-links ul { list-style: none; margin-top: 28px; }
  .quick-links li { font-size: 15px; line-height: 27.5px; }
  .quick-links a { color: var(--white); text-decoration: none; }
  .footer-rule { position: absolute; top: 345px; left: 0; width: 1200px; height: 1px; background: var(--footer-rule); }
  .copyright { position: absolute; top: 372px; width: 100%; text-align: center; font-family: var(--display);
    font-weight: 500; font-size: 14px; text-transform: uppercase; }
</style>
</head>
<body>

<header class="site-header">
  <div class="header-rule top"></div>
  <div class="header-rule bottom"></div>
  <div class="brand">
    <span class="brand-mark"></span>
    <span class="brand-name">Atelier Nine<br>Design Group</span>
  </div>
  <nav class="main-nav">
    <a class="active" href="#">Home</a>
    <a href="#">About</a>
    <a href="#">Team</a>
    <a href="#">Resedential</a>
    <a href="#">Commercial</a>
    <a href="#">Contact Us</a>
  </nav>
</header>

<section class="project-strip">
  <div class="project-photo photo-living" role="img" aria-label="Living room with green walls, patterned curtains, rattan pendant and cream sofa"></div>
  <div class="project-photo photo-bath" role="img" aria-label="Grey marble bathroom with freestanding white tub and wooden stool"></div>
  <div class="project-photo photo-study" role="img" aria-label="Study with styled shelving, dark desk and upholstered armchair"></div>
</section>

<section class="about-intro">
  <span class="intro-mark"></span>
  <h2 class="section-title">Who We Are</h2>
  <p class="intro-text">Lorem ipsum dolor sit amet, consectetur adipiscing elit, sed do eiusmod tempor incididunt ut labore et dolore magna aliqua. Ut enim ad minim veniam, quis nostrud exercitation ullamco laboris nisi ut aliquip ex ea commodo consequat. Duis aute irure dolor in reprehenderit in voluptate velit esse cillum dolore eu fugiat nulla pariatur. Excepteur sint occaecat cupidatat non proident, sunt in culpa qui officia deserunt mollit anim id est laborumSed ut perspiciatis unde omnis iste natus error sit voluptatem accusantium doloremque laudantium, totam rem aperiam, eaque ipsa quae ab illo inventore veritatis et quasi architecto beatae vitae dicta sunt explicabo. Nemo enim ipsam voluptatem quia voluptas sit aspernatur aut odit aut fugit, sed quia consequuntur magni dolores eos qui ratione voluptatem sequi nesciunt.</p>
  <a class="btn-outline" href="#">Learn More</a>
</section>

<section class="services">
  <h2 class="section-title">What We Do</h2>

  <article class="service commercial">
    <svg class="service-icon" viewBox="0 0 109 109" aria-hidden="true">
      <circle cx="54.5" cy="54.5" r="54.5" fill="var(--navy)"/>
      <g fill="var(--gold)">
        <rect x="38" y="32" width="20" height="46"/>
        <rect x="58" y="46" width="16" height="32"/>
      </g>
      <g fill="var(--navy)">
        <rect x="42" y="38" width="4" height="5"/><rect x="50" y="38" width="4" height="5"/>
        <rect x="42" y="49" width="4" height="5"/><rect x="50" y="49" width="4" height="5"/>
        <rect x="42" y="60" width="4" height="5"/><rect x="50" y="60" width="4" height="5"/>
        <rect x="62" y="52" width="3" height="5"/><rect x="68" y="52" width="3" height="5"/>
        <rect x="62" y="63" width="3" height="5"/><rect x="68" y="63" width="3" height="5"/>
      </g>
    </svg>
    <h3 class="service-name">Commercial</h3>
    <p class="service-text">Lorem ipsum dolor sit amet, consecteturhhsha&nbsp; a daxddip scing elit, sed do eiusmod tempncididunt ut labore et dolore magna aliqua.</p>
  </article>

  <article class="service residential">
    <svg class="service-icon" viewBox="0 0 109 109" aria-hidden="true">
      <circle cx="54.5" cy="54.5" r="54.5" fill="var(--navy)"/>
      <path d="M30 56L54.5 34L79 56H72V78H37V56Z" fill="var(--gold)"/>
      <rect x="49" y="62" width="11" height="16" fill="var(--navy)"/>
    </svg>
    <h3 class="service-name">Residential</h3>
    <p class="service-text">Lorem ipsum dolor sit amet, consecteturhhsha&nbsp; a daxddip scing elit, sed do eiusmod tempncididunt ut labore et dolore magna aliqua.</p>
  </article>
</section>

<footer class="site-footer">
  <div class="footer-contact">
    <h2 class="footer-title">Contact Us</h2>
    <ul class="contact-list">
      <li>
        <svg class="contact-icon" viewBox="0 0 31 31" aria-hidden="true"><circle cx="15.5" cy="15.5" r="15.5" fill="var(--gold)"/><path d="M15.5 7a5.5 5.5 0 0 0-5.5 5.5c0 4 5.5 10.5 5.5 10.5s5.5-6.5 5.5-10.5A5.5 5.5 0 0 0 15.5 7z" fill="var(--white)"/><circle cx="15.5" cy="12.5" r="2" fill="var(--gold)"/></svg>
        <span>123 ipsum dolor sit<br>amet, consectetur<br>adipiscing elit</span>
      </li>
      <li>
        <svg class="contact-icon" viewBox="0 0 31 31" aria-hidden="true"><circle cx="15.5" cy="15.5" r="15.5" fill="var(--gold)"/><path d="M10.5 8.5l3 0 1.5 4-2 1.5a9 9 0 0 0 4 4l1.5-2 4 1.5v3a1.5 1.5 0 0 1-1.5 1.5A13 13 0 0 1 9 10a1.5 1.5 0 0 1 1.5-1.5z" fill="var(--white)"/></svg>
        <span>+888 888 8888</span>
      </li>
      <li>
        <svg class="contact-icon" viewBox="0 0 31 31" aria-hidden="true"><circle cx="15.5" cy="15.5" r="15.5" fill="var(--gold)"/><rect x="8" y="10" width="15" height="11" rx="1.5" fill="var(--white)"/><path d="M8.5 11l7 5.5 7-5.5" stroke="var(--gold)" stroke-width="1.4" fill="none"/></svg>
        <span>info@atelierninedesign.example</span>
      </li>
    </ul>
  </div>

  <div class="footer-brand">
    <span class="brand-mark"></span>
    <span class="brand-name">Atelier Nine<br>Design Group</span>
  </div>
  <div class="social-links">
    <span aria-label="Social profile one"></span>
    <span aria-label="Social profile two"></span>
    <span aria-label="Social profile three"></span>
  </div>

  <nav class="quick-links">
    <h2 class="footer-title">Quick Links</h2>
    <ul>
      <li><a href="#">Home</a></li>
      <li><a href="#">About</a></li>
      <li><a href="#">Team</a></li>
      <li><a href="#">Resedential</a></li>
      <li><a href="#">Commercial</a></li>
      <li><a href="#">Contact us</a></li>
    </ul>
  </nav>

  <div class="footer-rule"></div>
  <p class="copyright">© 2022 Atelier Nine. All rights reserved</p>
</footer>

</body>
</html>
```